New Zealand Manuka Honey information banner

We are a Manuka honey export company and we are looking for a banner to show the benefits of our honey at trade shows.
Manuka honey and raw honey has a lot of health benefits and we would love you to open the creative beast inside you so that no one can walk passed our stand without stopping to read and purchase our products.
I have attached the shape of what it has to look like.
Full bleed size (artwork size)

850mm x 2060mm (10mm top and 50mm bottom)
10mm at the top for clamping purpose
50mm at the bottom to be attached to the spring machanism
Actual/Trim size (final size after mounting)
850mm x 2000mm
Note: Safe margin is 5mm from all edges (trim size)
Our role is to inform people what the benefits are of manuka honey and what the ratings mean between UMF, MGO and NPA

Target Market(s)

Health minded people

Industry/Entity Type

Health And Wellness

Font styles to use
Serif

Requirements
Must have
• Company name.. Kestrel Apiary NZ
• website... www.kestrelapiarynz.com
• Contact details kestrelapiarynz@postvale.com
• https://fx.qv/K83Tq17mzb
• There are two main components of Manuka honey which give it many health benefits:
• Hydrogen peroxide, a naturally antibiotic found in Manuka honey.
• Methylglyoxal (MG). A powerful antibiotic compound found in large quantities in Manuka honey.
• What is MGO?
• The MGO indicates the amount of Methylglyoxal in the honey. The higher the MGO rating the more antibacterial properties are in the honey.
• UMF MGO NPA
• 5+ 100+ 5
• 10+ 250+ 10
• 15+ 500+ 15
• 20+ 800+ 20
• Proven health Benefits of Active Manuka are
• Aiding in the treatment of:
• -Common Cold and Flu
• -sore throats
• -cuts and abrasions
• -Reduce hair loss and scalp problems
• -treating fungal infections
• -Burns
• -ulsers
• -strengthening the immune system
Nice to have
• Some bee related artwork in the background and something that relates our product to New Zealand
Should not have
• go crazy

```html
<!DOCTYPE html>
<html lang="en">
<head>
<meta charset="utf-8">
<title>Kestrel Apiary NZ – Banner</title>
<link href="https://fonts.googleapis.com/css2?family=Montserrat:wght@600;700;800&family=Raleway:wght@500;600;700&family=Oswald:wght@500&display=swap" rel="stylesheet">
<style>
  :root {
    --page: #e9ecef;
    --paper: #ffffff;
    --ink: #333333;
    --muted: #555555;
    --honey: #e8d52c;
    --amber: #e8a825;
    --table: #fdd835;
    --dark: #333333;
    --sky: #a9d3ee;
  }
  * { margin: 0; padding: 0; box-sizing: border-box; }
  html, body { width: 1183px; height: 1200px; overflow: hidden; background: var(--page); }
  .stage { position: relative; width: 1183px; height: 1200px; }
  .banner {
    position: absolute; left: 318px; top: 17px;
    width: 497px; height: 1060px;
    transform: scale(1.1); transform-origin: top left;
    background: var(--paper); overflow: hidden;
    box-shadow: 0 4px 18px rgba(0,0,0,.15);
  }
  .hero {
    position: absolute; left: 0; top: 0; width: 497px; height: 395px;
    background:
      radial-gradient(ellipse at 80% 40%, rgba(232,168,37,.35), transparent 45%),
      radial-gradient(ellipse at 12% 30%, rgba(214,120,170,.25), transparent 35%),
      linear-gradient(180deg, var(--sky) 0%, #d8ebf4 45%, #eef4f0 75%, var(--paper) 100%);
  }
  .side-bar { position: absolute; top: 213px; width: 8px; height: 172px; background: var(--honey); }
  .side-bar.left { left: 0; }
  .side-bar.right { right: 0; }
  .brand {
    position: absolute; top: 112px; left: 0; width: 100%;
    display: flex; justify-content: center; align-items: center; gap: 10px;
    font-family: 'Raleway', sans-serif; font-weight: 600; font-size: 29px; color: var(--ink);
  }
  .brand-dot { width: 14px; height: 14px; border-radius: 50%; background: var(--honey); }
  .headline {
    position: absolute; top: 168px; width: 100%; text-align: center;
    font-family: 'Montserrat', sans-serif; font-weight: 800; font-size: 26px;
    color: var(--ink); letter-spacing: -0.5px;
  }
  .benefits {
    position: absolute; top: 213px; width: 100%; list-style: none; text-align: center;
    font-family: 'Raleway', sans-serif; font-weight: 500; font-size: 18px; color: var(--ink);
    line-height: 28px;
  }
  .manuka-facts {
    position: absolute; top: 398px; left: 28px; width: 441px; text-align: center;
    font-family: 'Raleway', sans-serif; font-weight: 500; font-size: 10.5px;
    line-height: 14px; color: var(--ink);
  }
  .manuka-facts p + p { margin-top: 3px; }
  .manuka-facts strong { font-weight: 700; }
  .graphics { position: absolute; left: 0; top: 0; }
  .website {
    position: absolute; top: 964px; width: 100%; text-align: center;
    font-family: 'Montserrat', sans-serif; font-weight: 700; font-size: 25px; color: var(--ink);
  }
  .contact {
    position: absolute; left: 18px; top: 1015px; width: 460px; height: 45px;
    border-top: 2px solid #111; display: flex;
    font-family: 'Montserrat', sans-serif; font-weight: 700; font-size: 10.5px; color: var(--muted);
  }
  .contact-item { display: flex; align-items: center; gap: 6px; padding: 0 0 8px 0; height: 100%; }
  .contact-item + .contact-item { border-left: 2px solid #111; padding-left: 10px; }
  .contact-item:nth-child(1) { width: 135px; }
  .contact-item:nth-child(2) { width: 154px; }
  .contact-item svg { flex: none; }
</style>
</head>
<body>
<div class="stage">
  <div class="banner">
    <div class="hero" role="img" aria-label="Soft-focus photo of a honey jar with a wooden dipper among flowers under a blue sky"></div>
    <span class="side-bar left"></span>
    <span class="side-bar right"></span>

    <div class="brand"><span class="brand-dot"></span>Kestrel Apiary NZ Limited</div>
    <h1 class="headline">AIDING IN THE TREATMENT OF</h1>
    <ul class="benefits">
      <li>Common Cold and Flu</li>
      <li>Sore throats,Cuts and Abrasions</li>
      <li>Reduce hair loss and scalp problems</li>
      <li>Treating fungal infections</li>
      <li>Burns &amp; Ulsers</li>
      <li>Strengthening the Immune System</li>
    </ul>

    <div class="manuka-facts">
      <p><strong>There are two main components of Manuka honey which give it many health benefits:</strong></p>
      <p><strong>Hydrogen peroxide</strong>, a naturally antibiotic found in Manuka honey.</p>
      <p><strong>Methylglyoxal (MG)</strong>. A powerful antibiotic compound found in large quantities in Manuka honey.</p>
      <p><strong>What is MGO?</strong> The MGO indicates the amount of Methylglyoxal in the honey. The higher the MGO rating the more antibacterial properties are in the honey.</p>
    </div>

    <svg class="graphics" width="497" height="1060" viewBox="0 0 497 1060">
      <defs>
        <linearGradient id="beeTone" x1="0" y1="0" x2="0" y2="1">
          <stop offset="0" stop-color="#a77a68"/><stop offset=".55" stop-color="#b5533a"/><stop offset="1" stop-color="#d59a5e"/>
        </linearGradient>
        <linearGradient id="honeyTone" x1="0" y1="0" x2="0" y2="1">
          <stop offset="0" stop-color="#d8cfc6"/><stop offset=".6" stop-color="#b98a52"/><stop offset="1" stop-color="#7a4a1c"/>
        </linearGradient>
        <linearGradient id="careTone" x1="0" y1="0" x2="1" y2="0">
          <stop offset="0" stop-color="#3f6fae"/><stop offset=".6" stop-color="#d9c9c2"/><stop offset="1" stop-color="#eeeeee"/>
        </linearGradient>
        <clipPath id="tableHex"><polygon points="101,537 189,588 189,690 101,740 14,690 14,588"/></clipPath>
      </defs>

      <g class="honeycomb" transform="translate(36,157) scale(.85)">
        <polygon points="146,445 187,469 187,516 146,540 105,516 105,469" fill="var(--honey)"/>

        <polygon points="334,415 473,493 473,655 334,733 196,655 196,493" fill="url(#beeTone)" stroke="var(--amber)" stroke-width="4" role="img" aria-label="Close-up photo of a honey bee on a comb"/>

        <g class="rating-table" clip-path="url(#tableHex)" font-family="Oswald, sans-serif" font-size="11" fill="#111" text-anchor="middle">
          <rect x="0" y="530" width="200" height="220" fill="var(--dark)"/>
          <rect x="15" y="575" width="174" height="130" fill="var(--table)"/>
          <g stroke="#333" stroke-width="1">
            <line x1="73" y1="575" x2="73" y2="705"/>
            <line x1="131" y1="575" x2="131" y2="705"/>
            <line x1="15" y1="605" x2="189" y2="605"/>
            <line x1="15" y1="630" x2="189" y2="630"/>
            <line x1="15" y1="655" x2="189" y2="655"/>
            <line x1="15" y1="680" x2="189" y2="680"/>
          </g>
          <text x="44" y="595">UMF</text><text x="102" y="595">MGO</text><text x="160" y="595">NPA</text>
          <text x="44" y="621">5+</text><text x="102" y="621">100+</text><text x="160" y="621">5</text>
          <text x="44" y="646">10+</text><text x="102" y="646">250+</text><text x="160" y="646">10</text>
          <text x="44" y="671">15+</text><text x="102" y="671">500+</text><text x="160" y="671">15</text>
          <text x="44" y="696">20+</text><text x="102" y="696">800+</text><text x="160" y="696">20</text>
        </g>

        <polygon points="223,687 331,749 331,871 223,933 116,871 116,749" fill="url(#honeyTone)" role="img" aria-label="Photo of honey dripping onto a wooden spoon"/>
        <polygon points="416,697 487,738 487,821 416,862 345,821 345,738" fill="url(#careTone)" role="img" aria-label="Photo of a nurse applying a dressing to a hand"/>

        <polygon points="86,751 105,762 105,784 86,795 67,784 67,762" fill="var(--honey)"/>
        <polygon points="367,861 393,876 393,906 367,921 341,906 341,876" fill="var(--honey)"/>
      </g>
    </svg>

    <div class="website">www.kestrelapiarynz.com</div>

    <div class="contact">
      <div class="contact-item">
        <svg width="12" height="16" viewBox="0 0 12 16"><path d="M6 0a6 6 0 0 0-6 6c0 4.5 6 10 6 10s6-5.5 6-10a6 6 0 0 0-6-6z" fill="var(--honey)"/><circle cx="6" cy="6" r="2.3" fill="#fff"/></svg>
        <span>Your city address</span>
      </div>
      <div class="contact-item">
        <svg width="14" height="14" viewBox="0 0 24 24"><path d="M6.6 10.8a15.1 15.1 0 0 0 6.6 6.6l2.2-2.2a1 1 0 0 1 1-.25 11.4 11.4 0 0 0 3.6.57 1 1 0 0 1 1 1V20a1 1 0 0 1-1 1A17 17 0 0 1 3 4a1 1 0 0 1 1-1h3.5a1 1 0 0 1 1 1c0 1.250.2 2.45.57 3.6a1 1 0 0 1-.25 1z" fill="var(--honey)"/></svg>
        <span>+64 21 555 0198</span>
      </div>
      <div class="contact-item">
        <svg width="13" height="13" viewBox="0 0 16 16"><circle cx="8" cy="4.5" r="3.8" fill="var(--honey)"/><path d="M0 16c0-4 3.6-6.5 8-6.5s8 2.5 8 6.5z" fill="var(--honey)"/></svg>
        <span>kestrelapiarynz@postvale.com</span>
      </div>
    </div>
  </div>
</div>
</body>
</html>
```